Health care finance company startup website design

This design brief is for Ledger Nest, a small start-up company dealing with an online health care (initially dental targeted with plans for medical market) financial suite of tools. My business partners and I are looking to have a website developed for our business model.

We have developed a professional logo and would like it incorporated into the site. We are open to modifications on the logo if needed to accomplish the right design.

Our concept is a clean, simple design with a professional polish and very up-to-date web presence. The functionality of the site is simple yet powerful and we would like it’s design to complement that (including anticipated css3/html5 effects for an added dimension of UI polish).

We would like to see a design mockup of the functional elements of our site as our home page. We would also be very interested to see how your design would flow into the other pages such as search for a loan, create a payment plan, make a payment, sign in, registration, contact us and learn more.

Regarding Functional Elements:

-Simplicity is king.

-The three main functions of the site are the focus. They will operate via a series of API’s to webservices on the back-end, making the front end field focused, though we hope to have it feel friendly and simple.
-Search for a loan
-Create a payment plan
-Make a payment

Other functions of the site include:

-Sign in module
-We plan to support Kindlebook Link, Vornix Authentication and TrellisKey so incorporating design for those options is a plus.

-Registration module
-Two service levels clients can register for, loans only or loans & payments
-The registration process should be divided into sections with navigation back and forth until a confirmation final screen with pdf generations and remaining “to-do items” listed.
-The registration information will be saved in our database and also auto-populate fields for PDF’s that will be generated from templates.
-The registration will send a confirmation email and support TrellisKey, Vornix Authentication and Kindlebook Link, so designs should take these programmatic features into account.

-Contact us
-This will emphasize digital forms of communication (email and form submitted contact request).

-Learn more
-Explanations/faqs/tutorials
-This will contain video demonstrations/screencasts of key functions of website features

Regarding Design Elements:
-We want to be “wow’d” and don’t mind a surprise that redefines what we thought we liked regarding design.
-The following examples indicate some of the color schemes we like and design elements we hope to incorporate.
-We also recognize there is no substitute for creativity and originality.

Favorite Website Design Examples:

http://www.joginmarla.example/
HD backgrounds are a plus.
These colors are great.
The bright splashes of blue, red and orange combined with black in these shades.
A predominant background of whitesmoke or beige.

https://tillbrook.example/
The HD backgrounds are sharp.
The look is very clean (though it has a slight Quince computers imitation).
The left to right “scrolling” is preferable to vertical scrolling.
Very pleasing to the eye.

http://www.quarryfilmworks.example/
Again, use of bright, vibrant HD graphics is exceptional.
The left to right scrolling navigation is slick and likely how we would like our services to flow.

http://latest.wanderpelmark.example/
Love the look, feel and concepts in this site’s design
Especially colors and “photography” elements.
Updates

We've seen a few common themes in various designs submitted so far and want to add a few suggestions as we enter the final week of our design contest.

We do not want any photos of healthcare professionals or close-ups of people (families or couples or individuals).  Although we are a health care company we don't want to fall into a cliche feel for our site.  Instead we would like either objects or abstract images that have depth and are high definition, spanning from edge to edge of the width of the screen. 

We prefer shades of grey for the base color scheme with highlights of bright colors.  Please refer to the examples on the brief and use those as the best guide of what we want.  Even SketchGuild's color scheme is closer to what we want than some of the submissions, so please take note of the "shades of grey" with splashes of bright accent colors.

We love the horizontal navigation bar like that seen in the quarry filmworks site and anticipate our final product using a similar transition between the functions of the site.

Good luck to you all.  We are still looking for that WOW factor and hoping to see something original, that breaks the traditional mold and has a feel like the examples posted.

```html
<!DOCTYPE html>
<html lang="en">
<head>
<meta charset="utf-8">
<title>Ledger Nest – Home</title>
<link rel="stylesheet" href="https://fonts.googleapis.com/css2?family=Acme&family=Noto+Sans:wght@400;700&family=Open+Sans:wght@300;400;600&display=swap">
<style>
:root{
  --sky-deep:#0b5f96;
  --sky-mid:#1a8fcc;
  --sky-light:#5cc3ef;
  --navy:#13304f;
  --ink:#05070c;
  --white:#ffffff;
  --muted:#b7c3cc;
  --gold:#ffc61a;
  --gold-deep:#f6a400;
  --cyan:#1fd0f0;
  --band:#0a4f86;
}
*{box-sizing:border-box;margin:0;padding:0}
html,body{width:1138px;height:1200px;overflow:hidden}
body{
  position:relative;
  font-family:"Noto Sans",sans-serif;
  color:var(--white);
  background:
    radial-gradient(ellipse 700px 220px at 560px 1010px,rgba(190,235,255,.55),transparent 70%),
    radial-gradient(ellipse 500px 420px at 860px 260px,rgba(130,210,245,.45),transparent 70%),
    linear-gradient(180deg,#1e9ad6 0%,var(--sky-mid) 30%,var(--sky-deep) 60%,#1b7fbf 80%,#4fb4e4 95%);
}
.abs{position:absolute}

/* brand */
.brand{left:47px;top:26px;display:flex;align-items:center;gap:20px}
.brand-square{width:76px;height:76px;border-radius:10px;background:var(--navy)}
.brand-name{font-family:"Open Sans",sans-serif;font-weight:300;font-size:56px;color:var(--navy);letter-spacing:1px}

/* sign in */
.signin{left:818px;top:0;width:230px;height:63px;background:rgba(120,210,235,.55);border:2px solid rgba(190,240,255,.8);border-top:none;border-radius:0 0 8px 8px;padding:4px 8px}
.signin-field{height:22px;border:1px solid rgba(220,250,255,.85);background:rgba(40,130,170,.5);font-size:11px;padding:3px 8px;margin-bottom:5px;width:180px;color:#e8fbff}
.signin-go{position:absolute;right:-26px;top:16px;width:34px;height:14px}
.register{left:825px;top:70px;font-family:"Acme",sans-serif;font-size:25px;letter-spacing:.5px;text-shadow:0 2px 3px rgba(0,0,0,.35)}

/* hero */
.hero{left:47px;top:192px;font-family:"Acme",sans-serif;font-size:50px;line-height:55px;text-shadow:0 3px 4px rgba(0,0,0,.4)}
.hero-accent{color:var(--gold);text-transform:uppercase}

/* navigation */
.nav{left:41px;top:439px;width:1037px;height:146px;background:var(--ink);border-radius:12px}
.nav-tab{left:62px;top:419px;width:128px;height:210px;border-radius:14px;background:linear-gradient(180deg,#ffdd45,var(--gold-deep));box-shadow:0 2px 6px rgba(0,0,0,.35)}
.nav-drag{left:72px;top:588px;font-family:"Noto Sans",sans-serif;font-weight:700;font-size:15px;color:#3a2a00;display:flex;align-items:center;gap:10px}
.nav-drag-knob{width:30px;height:30px;border-radius:50%;background:#ffe46a;box-shadow:inset 0 -2px 3px rgba(0,0,0,.2)}
.nav-item{position:absolute;top:466px;width:130px;margin-left:-65px;text-align:center;font-size:14px;line-height:17px;color:var(--muted)}
.nav-item svg{display:block;margin:0 auto 8px;width:48px;height:48px}
.nav-item.is-active{color:var(--gold-deep);z-index:2}

/* welcome */
.welcome-title{left:45px;top:668px;font-family:"Open Sans",sans-serif;font-weight:300;font-size:34px;color:var(--navy)}
.welcome-title span{color:var(--gold);font-size:46px;margin-left:6px}
.welcome-copy{left:41px;top:738px;width:590px;font-size:19px;line-height:22.5px}
.welcome-copy p+p{margin-top:22px}

/* tweets */
.tweets-mark{left:688px;top:652px;width:58px;height:74px;border-radius:50%;background:radial-gradient(circle at 45% 45%,#ff8a3a,#e0511a)}
.tweets-title{left:764px;top:676px;font-family:"Open Sans",sans-serif;font-size:31px;color:var(--gold)}
.tweet{position:absolute;left:697px;width:365px}
.tweet-avatar{position:absolute;left:0;top:0;width:59px;height:50px;background:linear-gradient(180deg,#e8c79a,#b98a5c);border:1px solid #fff}
.tweet-text{margin-left:70px;font-size:14px;line-height:16px;padding-top:4px;min-height:50px}
.tweet-rule{margin-left:69px;border-top:1px dashed #fff}
.tweet-meta{margin-left:75px;margin-top:5px;font-size:14px;color:var(--navy)}
.tweet-meta span{color:var(--gold)}
.tweets-more{left:933px;top:944px;font-family:"Open Sans",sans-serif;font-size:19px;color:#7fd3f5;display:flex;align-items:center;gap:8px}

/* footer */
.foot-head{position:absolute;top:1048px;font-size:14px;color:var(--navy)}
.foot-links{position:absolute;top:1083px;font-size:12px;line-height:18.5px;color:var(--navy);list-style:none}
.newsletter-input{left:461px;top:1082px;width:181px;height:21px;background:var(--navy);border:1px solid #6aa5c8;font-size:10px;color:#8fb4cc;padding:3px 6px}
.newsletter-submit{left:461px;top:1109px;width:87px;height:28px;background:var(--cyan);border:2px solid #0f8aa8;color:var(--navy);font-size:13px;font-weight:700;text-align:center;line-height:24px}
.social{left:700px;top:1084px;display:flex;gap:8px}
.social i{display:block;width:27px;height:27px;border-radius:50%;background:radial-gradient(circle at 40% 35%,#8fdcff,#1a6fb0);border:1px solid #dff4ff}
.contact{position:absolute;left:910px;display:flex;align-items:center;gap:14px;font-size:15px}
.bottom-band{left:0;top:1163px;width:1138px;height:37px;background:linear-gradient(180deg,var(--band),#083c68)}
</style>
</head>
<body>

<div class="abs brand">
  <div class="brand-square"></div>
  <div class="brand-name">LEDGER NEST</div>
</div>

<div class="abs signin">
  <div class="signin-field">User id</div>
  <div class="signin-field">••••••••••••••</div>
  <svg class="signin-go" viewBox="0 0 34 14"><path d="M2 2l5 5-5 5M12 2l5 5-5 5M22 2l5 5-5 5" fill="none" stroke="#fff" stroke-width="3"/></svg>
</div>
<div class="abs register">REGISTER NOW!</div>

<h1 class="abs hero">To become the premier financial<br>services suite in the<br><span class="hero-accent">Dental/Medical Community.</span></h1>

<div class="abs nav-tab"></div>
<div class="abs nav-drag"><span class="nav-drag-knob"></span>DRAG</div>
<nav class="abs nav"></nav>

<div class="nav-item is-active" style="left:124px">
  <svg viewBox="0 0 48 48"><path d="M24 6L3 25h7v17h11V31h6v11h11V25h7z" fill="#f6a400"/></svg>Home</div>
<div class="nav-item" style="left:266px">
  <svg viewBox="0 0 48 48" fill="none" stroke="#55595f" stroke-width="3"><circle cx="24" cy="24" r="15"/><path d="M24 3v14M24 31v14M3 24h14M31 24h14"/></svg>Mission</div>
<div class="nav-item" style="left:413px">
  <svg viewBox="0 0 48 48"><path d="M24 4l18 8-18 8-18-8z" fill="#6a6e74"/><path d="M6 15l16 7v22L6 37z" fill="#55595f"/><path d="M42 15l-16 7v22l16-7z" fill="#45494f"/></svg>Product</div>
<div class="nav-item" style="left:561px">
  <svg viewBox="0 0 48 48" fill="none" stroke="#55595f" stroke-width="4"><circle cx="29" cy="18" r="12"/><path d="M20 27L5 43"/></svg>Search For A<br>Loan</div>
<div class="nav-item" style="left:703px">
  <svg viewBox="0 0 48 48"><rect x="9" y="3" width="30" height="42" rx="3" fill="#55595f"/><rect x="13" y="7" width="22" height="9" fill="#1b1d21"/><g fill="#1b1d21"><rect x="13" y="20" width="5" height="5"/><rect x="21" y="20" width="5" height="5"/><rect x="29" y="20" width="5" height="5"/><rect x="13" y="28" width="5" height="5"/><rect x="21" y="28" width="5" height="5"/><rect x="29" y="28" width="5" height="5"/><rect x="13" y="36" width="5" height="5"/><rect x="21" y="36" width="5" height="5"/><rect x="29" y="36" width="5" height="5"/></g></svg>Create A<br>Payment Plan</div>
<div class="nav-item" style="left:849px">
  <svg viewBox="0 0 48 48" fill="none" stroke="#55595f" stroke-width="5"><path d="M33 13c-2-3-5-4-9-4-5 0-9 2-9 6 0 9 19 5 19 14 0 4-4 7-10 7-4 0-8-2-10-5M24 2v44"/></svg>Make A<br>Payment</div>
<div class="nav-item" style="left:993px">
  <svg viewBox="0 0 48 48"><rect x="3" y="9" width="42" height="30" fill="#55595f"/><path d="M4 10l20 16 20-16M4 38l15-14M44 38L29 24" fill="none" stroke="#1b1d21" stroke-width="3"/></svg>Get in<br>Touch</div>

<h2 class="abs welcome-title">Welcome to<span>LEDGER NEST</span></h2>
<div class="abs welcome-copy">
  <p>Lorem ipsum dolor sit amet, consectetur adipiscing elit. Aenean iaculis faucibus magna, sed viverra metus lacinia non. Quisque et sapien varius massa convallis ornare. Quisque eget sem ante, porttitor rhoncus justo.</p>
  <p>Nunc at quam ut dui tincidunt malesuada. Donec varius tincidunt fringilla. In hac habitasse platea dictumst. Donec sodales, nulla eget iaculis tempus, sapien lacus viverra sem, vel molestie nibh libero non lacus.</p>
</div>

<div class="abs tweets-mark" role="img" aria-label="Orange cartoon bird mascot"></div>
<h3 class="abs tweets-title">Latest Tweets</h3>

<article class="tweet" style="top:746px">
  <div class="tweet-avatar" role="img" aria-label="Profile photo of the author"></div>
  <p class="tweet-text">Lorem ipsum dolor sit amet, consectetur adipiscing elit.</p>
  <div class="tweet-rule"></div>
  <p class="tweet-meta">Owen Pratt, <span>CEO Brightmoor.example</span></p>
</article>
<article class="tweet" style="top:847px">
  <div class="tweet-avatar" role="img" aria-label="Profile photo of the author"></div>
  <p class="tweet-text">Lorem ipsum dolor sit amet, consectetur adipiscing elit.</p>
  <div class="tweet-rule"></div>
  <p class="tweet-meta">Owen Pratt, <span>CEO Brightmoor.example</span></p>
</article>
<div class="abs tweets-more">More Tweets
  <svg width="20" height="20" viewBox="0 0 20 20" fill="none" stroke="#7fd3f5" stroke-width="2"><circle cx="10" cy="10" r="8"/><path d="M6 10h8M10 6l4 4-4 4"/></svg>
</div>

<footer>
  <h4 class="foot-head" style="left:56px">Quick Links</h4>
  <ul class="foot-links" style="left:63px"><li>Home</li><li>Mission</li><li>product</li></ul>
  <ul class="foot-links" style="left:145px"><li>Search For A Loan</li><li>Create a Payment Plan</li><li>Make A Payment</li></ul>
  <ul class="foot-links" style="left:309px"><li>Lorel Ipsum</li><li>Nuno Valencia</li><li>Esta di Maria</li></ul>

  <h4 class="foot-head" style="left:461px">Subscribe Newsletter</h4>
  <div class="abs newsletter-input">Type your email id</div>
  <div class="abs newsletter-submit">SUBMIT</div>

  <h4 class="foot-head" style="left:699px">Follow us</h4>
  <div class="abs social"><i></i><i></i><i></i><i></i><i></i></div>

  <h4 class="foot-head" style="left:903px">Call Us</h4>
  <div class="contact" style="top:1083px">
    <svg width="26" height="26" viewBox="0 0 26 26"><circle cx="13" cy="13" r="12" fill="#4fb4f0" stroke="#e6f7ff"/><path d="M9 7l3 3-2 2c1 2 2 3 4 4l2-2 3 3-2 2c-5 0-10-5-10-10z" fill="#fff"/></svg>
    555.014.0123</div>
  <div class="contact" style="top:1121px">
    <svg width="28" height="20" viewBox="0 0 28 20"><rect x="1" y="1" width="26" height="18" fill="#ffc61a"/><path d="M1 1l13 10 13-10" fill="none" stroke="#c98a00" stroke-width="2"/></svg>
    info@ledgernest.example</div>
</footer>

<div class="abs bottom-band"></div>
</body>
</html>
```